Fontenot Bayou Grillhouse (Owners Card)

Need a classy, but modern business card. I have included a promotional card for the steakhouse. I need one for myself (the owner) that is more professional.

Target Market(s)

General Public

Industry/Entity Type

Food service

Contact Information for Business Card

Name, business address, phone number, email, logo

Font styles to use
Serif
Sans Serif
Decorative
Script

Requirements
Must have
• My name (Darvel Pruitt), business address (327 Oakmere Street), phone number (510) 493-2615, email (Dpruittkr4@mailvane.example. On the back of the card: Psalms 27 1 The LORD is my light and my salvation— whom shall I fear? The LORD is the stronghold of my life— of whom shall I be afraid? 2 When the wicked advance against me to devour me, it is my enemies and my foes who will stumble and fall. 3 Though an army besiege me, my heart will not fear; though war break out against me, even then I will be confident.
Nice to have
• Something that’s bold, but modern and professional.

```html
<!DOCTYPE html>
<html lang="en">
<head>
<meta charset="utf-8">
<title>Fontenot Bayou Grillhouse – Owner Business Card</title>
<link rel="stylesheet" href="https://fonts.googleapis.com/css2?family=Cinzel:wght@500&family=Poppins:wght@400;600&display=swap">
<style>
  :root {
    --backdrop: #2b2b2d;
    --card: #0b0b0b;
    --green: #2fae3a;
    --yellow: #f2c21a;
    --orange: #f07a1c;
    --red: #e4242a;
    --white: #f2f2f2;
    --spectrum: linear-gradient(90deg, var(--green) 0%, var(--green) 28%, var(--yellow) 55%, var(--orange) 75%, var(--red) 100%);
  }
  * { box-sizing: border-box; margin: 0; padding: 0; }
  html, body { width: 1200px; height: 801px; overflow: hidden; }
  body {
    background: var(--backdrop);
    display: flex;
    align-items: center;
    justify-content: center;
    gap: 40px;
    font-family: "Poppins", sans-serif;
  }
  .card {
    position: relative;
    width: 550px;
    height: 314px;
    background: var(--card);
    border-radius: 14px;
    box-shadow: 0 10px 30px rgba(0,0,0,.45);
    overflow: hidden;
  }
  .gradient-text {
    background: var(--spectrum);
    -webkit-background-clip: text;
    background-clip: text;
    color: transparent;
  }

  /* Back: scripture */
  .scripture {
    position: absolute;
    left: 34px; right: 30px; top: 38px;
    font-weight: 600;
    font-size: 13.6px;
    line-height: 1.42;
  }
  .scripture .heading { display: block; }
  .scripture .verse { display: block; padding-left: 16px; text-indent: -16px; margin-bottom: 16px; }
  .scripture .verse:first-of-type { margin-bottom: 16px; }

  /* Front: identity */
  .brand {
    position: absolute;
    left: 300px; top: 48px; width: 220px;
    display: flex; align-items: center; gap: 10px;
  }
  .brand-dot {
    flex: none;
    width: 34px; height: 34px; border-radius: 50%;
    background: var(--orange);
  }
  .brand-name {
    font-weight: 600;
    font-size: 17px;
    line-height: 1.15;
    color: var(--yellow);
  }
  .contacts {
    position: absolute;
    left: 316px; top: 150px;
    list-style: none;
    font-size: 11.5px;
    color: var(--white);
  }
  .contacts li { display: flex; align-items: center; gap: 8px; height: 24px; }
  .contacts svg { width: 13px; height: 13px; flex: none; }
  .holder {
    position: absolute;
    left: 40px; top: 214px;
    text-align: right;
  }
  .holder-name {
    font-family: "Cinzel", serif;
    font-weight: 500;
    font-size: 29px;
    letter-spacing: .5px;
    line-height: 1;
    display: inline-block;
  }
  .holder-role {
    display: block;
    margin-top: 2px;
    padding-right: 40px;
    font-size: 12px;
    letter-spacing: 1.5px;
    color: var(--white);
  }
</style>
</head>
<body>

<section class="card card-back" aria-label="Card back">
  <p class="scripture gradient-text">
    <span class="heading">Psalms 27</span>
    <span class="verse">1 The LORD is my light and my salvation— whom shall I fear? The LORD is the stronghold of my life— of whom shall I be afraid?</span>
    <span class="verse">2 When the wicked advance against me to devour me, it is my enemies and my foes who will stumble and fall.</span>
    <span class="verse">3 Though an army besiege me, my heart will not fear; though war break out against me, even then I will be confident.</span>
  </p>
</section>

<section class="card card-front" aria-label="Card front">
  <div class="brand">
    <span class="brand-dot"></span>
    <span class="brand-name">Fontenot Bayou Grillhouse</span>
  </div>

  <ul class="contacts">
    <li>
      <svg viewBox="0 0 16 16"><path fill="var(--orange)" d="M3.5 1.5l2.5 3-1.5 1.5c.8 2 2.5 3.7 4.5 4.5l1.5-1.5 3 2.5-1.5 2.5C6.5 13.5 2.5 9.5 1 3z"/></svg>
      (510) 493-2615
    </li>
    <li>
      <svg viewBox="0 0 16 16"><rect x="1" y="3" width="14" height="10" fill="var(--yellow)"/><path d="M1 3l7 6 7-6" fill="none" stroke="var(--card)" stroke-width="1.4"/></svg>
      Dpruittkr4@mailvane.example
    </li>
    <li>
      <svg viewBox="0 0 16 16"><circle cx="8" cy="8" r="6.5" fill="none" stroke="var(--orange)" stroke-width="1.4"/><path d="M1.5 8h13M8 1.5c-3 3.5-3 9.5 0 13M8 1.5c3 3.5 3 9.5 0 13" fill="none" stroke="var(--orange)" stroke-width="1.2"/></svg>
      Fontenotgrill.example
    </li>
    <li>
      <svg viewBox="0 0 16 16"><path fill="var(--green)" d="M8 1a5 5 0 00-5 5c0 3.5 5 9 5 9s5-5.5 5-9a5 5 0 00-5-5zm0 7a2 2 0 110-4 2 2 0 010 4z"/></svg>
      327 Oakmere Street
    </li>
  </ul>

  <div class="holder">
    <span class="holder-name gradient-text">DARVEL PRUITT</span>
    <span class="holder-role">OWNER</span>
  </div>
</section>

</body>
</html>
```